Business Card Design Project

I want a business card to give to new customers once I have finished a job. The card is to be used for referals from that customer. If they use it they receive $25 off their next bill and the new customer receives $25 off their bill. I'd like to use thye logo off my website www.leoduffyelectrical.com.au. Other colours I like are grey and red. Open to suggestions. The back of the card will have standard contact details.

Reason: Waiting on changes to the design I like.

Target Market(s)

famalies. eastern suburbs sydney.

Industry/Entity Type

Business

Requirements
Must have
• company logo. contact deatils back of card (company name, phone, website, email add.)

```html
<!DOCTYPE html>
<html lang="en">
<head>
<meta charset="utf-8">
<title>Leo Duffy Electrical – Business Card</title>
<link href="https://fonts.googleapis.com/css2?family=Jost:wght@300;400;500;800&display=swap" rel="stylesheet">
<style>
  :root {
    --page: #ffffff;
    --card-grey: #e6e6e6;
    --card-blue: #d9ebfb;
    --stripe: #ffffff;
    --stripe-soft: #ecf5fd;
    --brand-blue: #4aa8f0;
    --ink: #000000;
    --badge-grey: #9fa3a3;
    --badge-ring: #cfeff3;
    --badge-text: #ffffff;
  }
  * { box-sizing: border-box; margin: 0; padding: 0; }
  html, body {
    width: 1200px; height: 900px; overflow: hidden;
    background: var(--page);
    font-family: "Jost", "Futura", sans-serif;
  }
  .card {
    position: absolute; left: 168px; top: 185px;
    width: 867px; height: 528px;
    overflow: hidden;
    background: var(--card-grey);
    border-left: 2px solid #bdbdbd;
  }
  .card-backdrop { position: absolute; inset: 0; }
  .card-title {
    position: absolute; left: 16px; top: 24px;
    font-size: 61px; line-height: 1; color: var(--brand-blue);
    white-space: nowrap; letter-spacing: 1px;
  }
  .card-title .name { font-weight: 800; }
  .card-title .trade { font-weight: 300; }
  .card-phone {
    position: absolute; left: 16px; top: 90px;
    font-size: 62px; font-weight: 800; line-height: 1; color: var(--ink);
    letter-spacing: 2px;
  }
  .service-list {
    position: absolute; left: 16px; top: 170px;
    list-style: none;
    font-size: 28px; font-weight: 400; line-height: 40.3px; color: var(--ink);
  }
  .badge { position: absolute; left: 400px; top: 118px; width: 440px; height: 340px; }
  .card-web {
    position: absolute; left: 16px; top: 455px;
    font-size: 50px; font-weight: 800; line-height: 1; color: var(--brand-blue);
    letter-spacing: 1.2px; white-space: nowrap;
  }
</style>
</head>
<body>
  <div class="card">
    <svg class="card-backdrop" viewBox="0 0 867 528" width="867" height="528" aria-hidden="true">
      <polygon points="330,0 867,0 867,528 650,528 470,340 370,330 230,0" fill="var(--card-blue)"/>
      <polygon points="80,0 330,0 600,170 360,150" fill="var(--stripe)"/>
      <polygon points="200,0 330,0 620,150 520,150" fill="var(--stripe-soft)"/>
      <polygon points="0,110 380,120 0,40" fill="var(--stripe)"/>
      <polygon points="360,330 470,340 650,528 600,528" fill="var(--stripe)"/>
    </svg>

    <h1 class="card-title"><span class="name">LEO DUFFY</span> <span class="trade">ELECTRICAL</span></h1>
    <p class="card-phone">0400 555 123</p>

    <ul class="service-list">
      <li>residential</li>
      <li>commercial</li>
      <li>new and old</li>
      <li>lighting</li>
      <li>power</li>
      <li>phone/data/internet points</li>
      <li>and more</li>
    </ul>

    <svg class="badge" viewBox="0 0 440 340" width="440" height="340" role="img" aria-label="Leo Duffy Electrical">
      <circle cx="222" cy="165" r="160" fill="var(--badge-grey)" stroke="var(--badge-ring)" stroke-width="10"/>
      <text text-anchor="middle" font-family="Jost, sans-serif" font-weight="500" font-size="38" fill="var(--badge-text)">
        <tspan x="222" y="160">LEO DUFFY</tspan>
        <tspan x="222" y="204">ELECTRICAL</tspan>
      </text>
    </svg>

    <p class="card-web">www.leoduffyelectrical.com.au</p>
  </div>
</body>
</html>
```